Membership Drive "End of Spring Sale"

Looking to run a Direct Debit Sale for November 2019 to boost membership number up. This is our slowest area for membership growth, many choose not to do direct debit, special is designed to increase numbers. Artwork will be display via social media (FB and Instagram) as well as in store. Artwork must be eye catching and direct to the customer. Customer should feel a sense of relief with monthly payments instead of one large payment.

Heading: "End of Spring Special"
Direct Debit
$39.95 per month
Terms and conditions apply"
*Offer End 30th November

Slogan:
"More Energy
More Atmosphere
Feel the Difference
Make the change now" can be placed where suits.

below are other promos we had designed on Artwork Hive along with potential photos to be included into this promo

Target Market(s)

Males and Females aged between 18 - 40

Industry/Entity Type

Fitness

Colors

Designer to choose colors to be used in the design.

Requirements
Must have
• Must emphasize "End of Spring Special" $39.95 per month and
• under neath strict terms and conditions apply
• Offer Ends 30th of November
• "All of our contact details"
• Address: 14 Marlow Rd Brindle Park 3187
• Ph: 9581 2706
• www.pulsarfit.com.au
• Design format must come in poster size A0 size, Instagram format, Facebook cover and 800 x 800 for the website
Nice to have
• With the photos attached at least one female and one male in the overall design. Lots of color in relation to Spring and artistic effects to catch peoples eyes.
• Also to include "Celebrating 49 years"

```html
<!DOCTYPE html>
<html lang="en">
<head>
<meta charset="utf-8">
<title>Pulsar Fit – End of Spring Special</title>
<link rel="stylesheet" href="https://fonts.googleapis.com/css2?family=Oswald:wght@500;700&display=swap">
<style>
  :root {
    --red: #e8231d;
    --red-deep: #7a0d0b;
    --white: #ffffff;
    --ink: #0c0c0e;
    --steel: #2b2d33;
    --bar: #111114;
  }
  * { margin: 0; padding: 0; box-sizing: border-box; }
  html, body { width: 849px; height: 1200px; overflow: hidden; background: var(--ink); }
  .poster {
    position: relative; width: 849px; height: 1200px; overflow: hidden;
    font-family: "Oswald", sans-serif; color: var(--white);
  }
  .gym-backdrop {
    position: absolute; inset: 0;
    background:
      radial-gradient(ellipse 60% 35% at 55% 8%, rgba(232,35,29,.45), transparent 70%),
      radial-gradient(ellipse 50% 40% at 30% 55%, rgba(90,92,100,.35), transparent 70%),
      linear-gradient(180deg, #1b1b20 0%, #121215 55%, #0b0b0d 100%);
  }
  .athlete-male {
    position: absolute; left: 240px; top: 170px; width: 420px; height: 760px;
    border-radius: 180px 180px 60px 60px;
    background: radial-gradient(ellipse at 50% 35%, #a4684a 0%, #6b3e2b 45%, rgba(30,20,18,0) 75%);
  }
  .athlete-female {
    position: absolute; left: 580px; top: 700px; width: 269px; height: 290px;
    background: radial-gradient(ellipse at 55% 50%, #c98f70 0%, #6e4637 45%, rgba(20,15,14,0) 75%);
  }
  .brand {
    position: absolute; left: 26px; top: 14px; width: 104px; height: 104px;
    border-radius: 50%; background: var(--ink); border: 3px solid var(--white);
    display: flex; align-items: center; justify-content: center; text-align: center;
    font-weight: 700; font-size: 22px; line-height: 1.05; color: var(--white);
  }
  .headline {
    position: absolute; right: 40px; top: 30px; text-align: center;
    font-weight: 700; font-size: 72px; line-height: 1.05; color: var(--red);
    text-transform: uppercase;
  }
  .offer { position: absolute; left: 40px; top: 212px; }
  .price { display: flex; align-items: flex-end; font-weight: 700; line-height: 1; }
  .price-amount { font-size: 74px; }
  .price-period { font-size: 26px; margin: 0 0 8px 8px; }
  .terms { color: var(--red); font-size: 20px; font-weight: 500; margin-top: 8px; }
  .deadline { color: var(--red); font-size: 27px; font-weight: 500; line-height: 1.2; margin-top: 12px; }
  .slogan { position: absolute; left: 40px; top: 520px; list-style: none; }
  .slogan li { font-weight: 700; font-size: 54px; line-height: 1.06; text-transform: uppercase; }
  .slogan .accent { color: var(--red); }
  .anniversary {
    position: absolute; left: 0; right: 0; top: 1000px; text-align: center;
    font-weight: 700; font-size: 86px; color: var(--red); text-transform: uppercase; line-height: 1;
  }
  .contact-bar {
    position: absolute; left: 0; right: 0; bottom: 0; height: 80px; background: var(--bar);
    display: flex; align-items: center; justify-content: space-around; padding: 0 20px;
    font-weight: 500; font-size: 22px;
  }
  .contact-item { display: flex; align-items: center; gap: 10px; }
  .contact-item svg { width: 26px; height: 26px; fill: var(--red); }
</style>
</head>
<body>
<main class="poster">
  <div class="gym-backdrop" role="img" aria-label="Dark gym interior with red lighting"></div>
  <div class="athlete-male" role="img" aria-label="Muscular man lifting a weight plate"></div>
  <div class="athlete-female" role="img" aria-label="Woman in boxing gloves in fighting stance"></div>

  <div class="brand">PULSAR<br>FIT</div>

  <h1 class="headline">End of<br>Spring Special</h1>

  <section class="offer">
    <div class="price"><span class="price-amount">$39.95</span><span class="price-period">MONTH</span></div>
    <p class="terms">Terms and conditions apply</p>
    <p class="deadline">Offer Ends<br>30th of November</p>
  </section>

  <ul class="slogan">
    <li class="accent">More Energy</li>
    <li>More Atmosphere</li>
    <li class="accent">Feel the Difference</li>
    <li>Make the Change Now</li>
  </ul>

  <p class="anniversary">Celebrating 49 Years</p>

  <footer class="contact-bar">
    <span class="contact-item">
      <svg viewBox="0 0 24 24"><path d="M12 2a7 7 0 0 0-7 7c0 5 7 13 7 13s7-8 7-13a7 7 0 0 0-7-7zm0 9.5A2.5 2.5 0 1 1 12 6.5a2.5 2.5 0 0 1 0 5z"/></svg>
      14 Marlow Rd Brindle Park 3187
    </span>
    <span class="contact-item">
      <svg viewBox="0 0 24 24"><path d="M6.6 10.8a15 15 0 0 0 6.6 6.6l2.2-2.2a1 1 0 0 1 1-.25 11.4 11.4 0 0 0 3.6.57 1 1 0 0 1 1 1V20a1 1 0 0 1-1 1A17 17 0 0 1 3 4a1 1 0 0 1 1-1h3.5a1 1 0 0 1 1 1c0 1.25.2 2.45.57 3.57a1 1 0 0 1-.25 1z"/></svg>
      9581 2706
    </span>
    <span class="contact-item">
      <svg viewBox="0 0 24 24"><path d="M12 2a10 10 0 1 0 0 20 10 10 0 0 0 0-20zm6.9 6h-2.9a15.7 15.7 0 0 0-1.4-3.6A8 8 0 0 1 18.9 8zM12 4a14 14 0 0 1 1.9 4h-3.8A14 14 0 0 1 12 4zM4.3 14a8 8 0 0 1 0-4h3.4a16.5 16.5 0 0 0 0 4zm.8 2h2.9a15.7 15.7 0 0 0 1.4 3.6A8 8 0 0 1 5.1 16zM8 8H5.1a8 8 0 0 1 4.3-3.6A15.7 15.7 0 0 0 8 8zm4 12a14 14 0 0 1-1.9-4h3.8A14 14 0 0 1 12 20zm2.3-6H9.7a14.7 14.7 0 0 1 0-4h4.6a14.7 14.7 0 0 1 0 4zm.3 5.6a15.7 15.7 0 0 0 1.4-3.6h2.9a8 8 0 0 1-4.3 3.6zm1.7-5.6a16.5 16.5 0 0 0 0-4h3.4a8 8 0 0 1 0 4z"/></svg>
      WWW.PULSARFIT.COM.AU
    </span>
  </footer>
</main>
</body>
</html>
```